Managed Services Provider for Medical Practices Business Card Design

We need a business card design for a new company based in the Illawarra region on NSW Australia, with intentions of expanding further into other regions. We provide I.T. managed services, server, printer, phone and hardware procurement and installations. We specialise in Medical Practices e.g. General Practitioners, Surgeons and other medical specialists etc. We would like to see colours that theme with our website. The final design should communicate integrity, strength, security and reliability.

Industry/Entity Type

Security

Contact Information for Business Card

Kelbury Vitalink, Corey Baldock, Shop 9 Brenwick Arcade, 147 Marlowe Fenton Road Wendabri WA 6117, Partner - Senior Technician, Ph: 0491 637 528, Email: corey@vitalink.net.au, Web: www.vitalink.net.au

Kelbury Vitalink, Liam Pettifer, Shop 9 Brenwick Arcade, 147 Marlowe Fenton Road Wendabri WA 6117, Partner - Senior Technician, Ph: 0427 519 843, Email: liam@vitalink.net.au, Web: www.vitalink.net.au

```html
<!DOCTYPE html>
<html lang="en">
<head>
<meta charset="utf-8">
<title>Kelbury Vitalink – Business Card</title>
<link rel="stylesheet" href="https://fonts.googleapis.com/css2?family=Open+Sans:wght@400;600;700&display=swap">
<style>
  :root {
    --brand-green: #57bb48;
    --card-charcoal: #3b3b3d;
    --ink-white: #ffffff;
    --ink-soft: #e6e6e6;
    --stage: #9a9a9a;
  }
  * { margin: 0; padding: 0; box-sizing: border-box; }
  html, body {
    width: 1200px; height: 900px; overflow: hidden;
    background: var(--stage);
    font-family: "Open Sans", Arial, sans-serif;
  }
  .canvas { position: relative; width: 1200px; height: 900px; }

  .card {
    position: absolute;
    width: 520px; height: 318px;
    overflow: hidden;
    box-shadow: 0 10px 24px rgba(0,0,0,0.25);
  }

  /* Front */
  .card--front { left: 70px; top: 110px; background: var(--brand-green); }
  .card--front .wordmark {
    position: absolute; right: 46px; top: 118px;
    display: flex; align-items: center; gap: 10px;
  }
  .wordmark-name {
    font-weight: 700; font-size: 38px; letter-spacing: -0.5px;
    color: var(--ink-white); line-height: 1; text-transform: lowercase;
    white-space: nowrap;
  }
  .wordmark-dot { width: 14px; height: 14px; background: var(--ink-white); }
  .card--front .tagline {
    position: absolute; right: 46px; top: 168px;
    font-size: 19px; color: var(--ink-white); letter-spacing: 0.3px;
  }

  /* Back */
  .card--back { left: 620px; top: 470px; background: var(--card-charcoal); }
  .card--back .wordmark {
    position: absolute; right: 30px; top: 36px;
    display: flex; align-items: center; gap: 8px;
  }
  .card--back .wordmark-name { font-size: 32px; }
  .card--back .wordmark-dot { width: 12px; height: 12px; background: var(--brand-green); }
  .card--back .tagline {
    position: absolute; right: 30px; top: 78px;
    font-size: 16px; color: var(--brand-green); letter-spacing: 0.3px;
  }

  .name-band {
    position: absolute; left: 168px; right: 0; top: 128px; height: 26px;
    background: var(--brand-green);
  }
  .name-tab {
    position: absolute; left: 152px; top: 128px; width: 10px; height: 26px;
    background: var(--brand-green); transform: skewX(-12deg);
  }
  .holder-name {
    position: absolute; left: 180px; top: 130px;
    font-weight: 700; font-size: 16px; letter-spacing: 0.8px;
    color: var(--ink-white); text-transform: uppercase; line-height: 22px;
  }
  .holder-role {
    position: absolute; left: 176px; top: 160px;
    font-size: 12px; line-height: 16px; color: var(--ink-soft);
  }
  .accent-rule {
    position: absolute; left: 380px; right: 0; top: 166px; height: 12px;
    background: var(--brand-green);
  }

  .contact-list {
    position: absolute; left: 158px; top: 196px; list-style: none;
  }
  .contact-list li {
    display: flex; align-items: center; gap: 8px;
    font-size: 12.5px; color: var(--ink-white); height: 22px;
    white-space: nowrap;
  }
  .contact-list svg { width: 13px; height: 13px; flex: none; }

  .address {
    position: absolute; right: 26px; top: 214px;
    text-align: right; font-size: 10.5px; line-height: 19px; font-style: normal;
    color: var(--brand-green); text-transform: uppercase; letter-spacing: 0.4px;
    white-space: nowrap;
  }
  .base-band {
    position: absolute; left: 148px; right: 0; top: 276px; height: 9px;
    background: var(--brand-green);
  }
</style>
</head>
<body>
<main class="canvas">

  <section class="card card--front" aria-label="Business card front">
    <div class="wordmark">
      <span class="wordmark-name">Kelbury Vitalink</span>
      <span class="wordmark-dot"></span>
    </div>
    <p class="tagline">your technical specialists</p>
  </section>

  <section class="card card--back" aria-label="Business card back">
    <div class="wordmark">
      <span class="wordmark-name">Kelbury Vitalink</span>
      <span class="wordmark-dot"></span>
    </div>
    <p class="tagline">your technical specialists</p>

    <div class="name-tab"></div>
    <div class="name-band"></div>
    <h1 class="holder-name">Corey Baldock</h1>
    <div class="accent-rule"></div>
    <p class="holder-role">Partner - Senior Technician</p>

    <ul class="contact-list">
      <li>
        <svg viewBox="0 0 14 14" aria-hidden="true"><rect x="3" y="0.5" width="8" height="13" rx="1.5" fill="none" stroke="#57bb48" stroke-width="1.4"/><circle cx="7" cy="11" r="0.9" fill="#57bb48"/></svg>
        0491 637 528
      </li>
      <li>
        <svg viewBox="0 0 14 14" aria-hidden="true"><rect x="0.7" y="2.5" width="12.6" height="9" fill="none" stroke="#57bb48" stroke-width="1.4"/><path d="M1 3 L7 8 L13 3" fill="none" stroke="#57bb48" stroke-width="1.4"/></svg>
        corey@vitalink.net.au
      </li>
      <li>
        <svg viewBox="0 0 14 14" aria-hidden="true"><circle cx="7" cy="7" r="6" fill="none" stroke="#57bb48" stroke-width="1.4"/><path d="M1 7 H13 M7 1 C3.5 4 3.5 10 7 13 C10.5 10 10.5 4 7 1" fill="none" stroke="#57bb48" stroke-width="1.2"/></svg>
        www.vitalink.net.au
      </li>
    </ul>

    <address class="address">
      Shop 9 Brenwick Arcade<br>
      147 Marlowe Fenton<br>
      Road Wendabri WA 6117
    </address>

    <div class="base-band"></div>
  </section>

</main>
</body>
</html>
```